Ancient Art and Artifact information website

Hello Designers,
We are starting up a new website who talk abut and discusses an ancient arts artifacts. We would covering a wide range of countries ranging from Egypt, Greece, India, Syria, Rome, etc. My website name Brisk Loom
Designs that fits with ancient theme and some kind of uniqueness would be accepted.
Requirements:
1) A home page design
2) Sub page design
3) A suitable logo
Sections can be added are featured ancient arts/places with short description followed by a more button, latest news, and comment section.
Add contents if you found relevant for this category of website. Ability to share the information through social media is desired.
Must be a responsive design. I look forward to designs which are mind blowing.
2 page

```html
<!DOCTYPE html>
<html lang="en">
<head>
<meta charset="utf-8">
<title>Brisk Loom – Egypt</title>
<link href="https://fonts.googleapis.com/css2?family=Didact+Gothic&family=Roboto:wght@400;500;700&display=swap" rel="stylesheet">
<style>
:root{
  --gold:#c9a02c;
  --gold-dark:#8a6a14;
  --gold-text:#d8ae3a;
  --panel:#1c1c1c;
  --panel-2:#232323;
  --band:#4a4a4a;
  --ink:#9a9a9a;
  --ink-soft:#7d7d7d;
  --bg-1:#5a4420;
  --bg-2:#2a1f10;
  --bg-3:#0c0a07;
}
*{margin:0;padding:0;box-sizing:border-box}
html,body{width:802px;height:1200px;overflow:hidden}
body{
  position:relative;
  font-family:"Roboto",Arial,sans-serif;
  background:
    radial-gradient(ellipse 70% 30% at 50% 8%, var(--bg-1), transparent 70%),
    radial-gradient(ellipse 60% 20% at 50% 100%, #3d2e16, transparent 70%),
    linear-gradient(180deg, #4a381b 0%, var(--bg-2) 30%, var(--bg-3) 62%, #171209 88%, #3a2c14 100%);
}
.abs{position:absolute}

/* navigation */
.nav{left:96px;top:44px;width:610px;height:40px;background:#242424;border:1px solid #3b3b3b;border-radius:3px;box-shadow:0 2px 6px rgba(0,0,0,.6)}
.nav-inner{position:absolute;inset:4px;border:1px solid #3a3a3a}
.nav a{position:absolute;top:13px;font-family:"Didact Gothic",sans-serif;font-size:10px;color:#d9d0bd;text-decoration:none}
.nav a.active{color:var(--gold-text)}
.nav .login{top:11px;background:var(--gold);color:#1a1a1a;padding:1px 8px;font-size:10px}
.brand-plate{left:353px;top:20px;width:96px;height:88px;background:#262626;border:3px solid #3a3a3a;border-radius:6px;box-shadow:0 3px 8px rgba(0,0,0,.7);display:flex;align-items:center;justify-content:center;text-align:center}
.brand-name{font-family:"Roboto",sans-serif;font-weight:700;font-size:16px;line-height:17px;color:var(--gold);text-transform:uppercase}

/* ribbons */
.ribbon svg{display:block}
.ribbon-title{position:absolute;left:0;right:0;text-align:center;color:#f1e6c8;font-weight:500}

/* media placeholders */
.media{border-radius:2px}

/* article panel */
.article{left:96px;top:332px;width:610px;height:424px;background:var(--panel);border-radius:0 0 3px 3px}
.h-main{left:96px;top:350px;width:610px;text-align:center;font-size:15px;font-weight:500;color:var(--gold-text)}
.lead{left:128px;top:381px;width:546px;text-align:center;font-size:7.3px;line-height:12.2px;color:var(--ink)}
.rule{left:320px;top:446px;width:162px;height:1px;background:#333}
.h-sub{font-size:10px;font-weight:500;color:var(--gold-text)}
.copy{font-size:7.3px;line-height:12.2px;color:var(--ink)}
.btn{background:var(--gold);color:#2a2108;font-size:7px;font-weight:700;text-transform:uppercase;display:flex;align-items:center;justify-content:center;border:1px solid var(--gold-dark)}

/* cards */
.card{top:858px;width:194px;height:196px;background:var(--panel-2);box-shadow:0 2px 6px rgba(0,0,0,.6)}
.card .img{position:absolute;left:0;top:0;width:194px;height:102px}
.card .band{position:absolute;left:0;top:102px;width:194px;height:24px;background:var(--band);color:#eee;font-size:12px;font-weight:500;text-align:center;line-height:24px;letter-spacing:.3px}
.card .text{position:absolute;left:15px;top:137px;width:168px;font-size:7px;line-height:12px;color:var(--ink-soft)}
.card .sep{position:absolute;left:15px;top:167px;width:164px;height:1px;background:#3a3a3a}
.card .more{position:absolute;left:15px;top:173px;width:35px;height:13px}
.card .stats{position:absolute;right:15px;top:175px;font-size:6.5px;color:#8a8a8a;display:flex;gap:8px;align-items:center}
.stats svg{vertical-align:middle;margin-right:2px}
.arrow{top:944px;width:19px;height:19px;background:var(--gold);display:flex;align-items:center;justify-content:center}

/* footer */
.footer{left:0;top:1110px;width:802px;height:56px;background:#232323}
.foot-plate{left:96px;top:1092px;width:98px;height:92px;background:#262626;border:3px solid #3a3a3a;border-radius:6px;display:flex;align-items:center;justify-content:center;text-align:center;box-shadow:0 3px 8px rgba(0,0,0,.7)}
.foot-links{left:268px;top:1123px;width:280px;text-align:center;font-size:8.5px}
.foot-links a{color:var(--gold-text);text-decoration:none;margin:0 2px}
.copyright{left:268px;top:1144px;width:280px;text-align:center;font-size:5.6px;color:#555;letter-spacing:.3px}
.social{top:1130px;width:17px;height:17px;border-radius:50%;background:#555}
</style>
</head>
<body>

<nav class="abs nav">
  <div class="nav-inner"></div>
  <a href="#" style="left:17px">Home</a>
  <a href="#" class="active" style="left:68px">Ancient Arts</a>
  <a href="#" style="left:149px">History</a>
  <a href="#" style="left:206px">News</a>
  <a href="#" style="left:375px">Gallery</a>
  <a href="#" style="left:434px">Articles</a>
  <a href="#" style="left:494px">Contact</a>
  <a href="#" class="login" style="left:551px">Login</a>
</nav>
<div class="abs brand-plate"><span class="brand-name">Brisk<br>Loom</span></div>

<div class="abs ribbon" style="left:284px;top:120px;width:232px;height:42px">
  <svg width="232" height="42" viewBox="0 0 232 42">
    <polygon points="0,18 30,14 36,38 8,40 18,30" fill="#9a7a1c"/>
    <polygon points="232,18 202,14 196,38 224,40 214,30" fill="#9a7a1c"/>
    <polygon points="26,2 206,2 210,32 22,32" fill="var(--gold)"/>
  </svg>
  <div class="ribbon-title" style="top:6px;font-size:20px">Egypt</div>
</div>

<div class="abs media" role="img" aria-label="Carved Egyptian temple relief with hieroglyphs and figures of pharaohs" style="left:96px;top:176px;width:610px;height:156px;background:linear-gradient(135deg,#a57a3a,#7a5526 45%,#b38a48 70%,#6b4a22)"></div>

<div class="abs article"></div>
<h1 class="abs h-main">The standard Lorem Ipsum passage</h1>
<p class="abs lead">Sed ut perspiciatis unde omnis iste natus error sit voluptatem edusa accusantium doloremque laudantium, totam rem aperiam, eaque ipsa quae ab illo inventore veritatis et quasi architecto beatae vitae dicta sunt explicabo. Nemo enim ipsam voluptatem quia voluptas aspernatur odit aut fugit, sed quia consequuntur magni dolores eos qui ratione voluptatem sequi nesciunt. Neque porro quisquam est, qui dolorem ipsum quia dolor amet, consectetur, adipisci velit, sed quia non numquam eius modi tempora incidunt ut labore et dolore magnam aliquam quaerat voluptatem.</p>
<div class="abs rule"></div>

<div class="abs media" role="img" aria-label="Painted Egyptian wall relief of a figure" style="left:126px;top:472px;width:210px;height:110px;background:linear-gradient(120deg,#b98a5a,#9a5a34 50%,#c49a6c);box-shadow:0 2px 5px rgba(0,0,0,.6)"></div>
<h2 class="abs h-sub" style="left:358px;top:469px">The standard Lorem Ipsum passage, used since the 1500s</h2>
<p class="abs copy" style="left:358px;top:494px;width:322px">Sed ut perspiciatis unde omnis iste natus error sit voluptatem edusa accusantium doloremque laudantium, totam rem aperiam, eaque ipsa quae ab illo inventore veritatis et architecto beatae vitae dicta sunt explicabo. Nemo enim ipsam voluptatem quia voluptas aspernatur odit aut fugit, sed quia consequuntur magni dolores eos qui ratione voluptatem sequi nesciunt. Neque porro quisquam est, qui dolorem ipsum quia dolor amet, consectetur, adipisci velit, sed quia non numquam eius modi tempora incidunt ut labore et dolore magnam aliquam quaerat voluptatem vitae dicta sunt explicabo.</p>

<h2 class="abs h-sub" style="left:126px;top:606px">The standard Lorem Ipsum passage, used since the 1500s</h2>
<p class="abs copy" style="left:126px;top:631px;width:322px">Sed ut perspiciatis unde omnis iste natus error sit voluptatem edusa accusantium doloremque laudantium, totam rem aperiam, eaque ipsa quae ab illo inventore veritatis et architecto beatae vitae dicta sunt explicabo. Nemo enim ipsam voluptatem quia voluptas aspernatur odit aut fugit, sed quia consequuntur magni dolores eos qui ratione voluptatem sequi nesciunt. Neque porro quisquam est, qui dolorem ipsum quia dolor amet, consectetur, adipisci velit, sed quia non numquam eius modi tempora incidunt labore et dolore magnam aliquam quaerat voluptatem vitae dicta sunt explicabo.</p>
<div class="abs media" role="img" aria-label="Row of ram-headed sphinx statues before temple columns" style="left:466px;top:609px;width:211px;height:109px;background:linear-gradient(160deg,#7a6650,#b8a184 45%,#8d7a62);box-shadow:0 2px 5px rgba(0,0,0,.6)"></div>

<a class="abs btn" style="left:374px;top:734px;width:55px;height:13px;text-decoration:none">Load more</a>

<div class="abs ribbon" style="left:232px;top:792px;width:338px;height:44px">
  <svg width="338" height="44" viewBox="0 0 338 44">
    <polygon points="0,38 32,14 52,14 52,40" fill="#9a7a1c"/>
    <polygon points="338,38 306,14 286,14 286,40" fill="#9a7a1c"/>
    <polygon points="28,2 310,2 314,34 24,34" fill="var(--gold)"/>
  </svg>
  <div class="ribbon-title" style="top:4px;font-size:22px">Popular Ancient Arts</div>
</div>

<div class="abs arrow" style="left:61px"><svg width="8" height="8" viewBox="0 0 8 8"><path d="M5.5 1 L2.5 4 L5.5 7" stroke="#2a2108" stroke-width="1.4" fill="none"/></svg></div>
<div class="abs arrow" style="left:722px"><svg width="8" height="8" viewBox="0 0 8 8"><path d="M2.5 1 L5.5 4 L2.5 7" stroke="#2a2108" stroke-width="1.4" fill="none"/></svg></div>

<article class="abs card" style="left:95px">
  <div class="img" role="img" aria-label="Egyptian carved relief of deities" style="background:linear-gradient(135deg,#b08a4c,#7d5a28 60%,#a07a3e)"></div>
  <div class="band">Egypt</div>
  <p class="text">Sed ut perspiciatis unde omnis iste natus error sit voluptatem edusa accusant.</p>
  <div class="sep"></div>
  <a class="btn more" href="#" style="text-decoration:none">More</a>
  <div class="stats"><span><svg width="7" height="6" viewBox="0 0 7 6"><path d="M3.5 6 L0.5 3 A1.6 1.6 0 0 1 3.5 1 A1.6 1.6 0 0 1 6.5 3 Z" fill="#8a8a8a"/></svg>457</span><span><svg width="7" height="5" viewBox="0 0 7 5"><rect width="7" height="5" fill="#8a8a8a"/><path d="M0 0 L3.5 3 L7 0" stroke="#232323" stroke-width=".8" fill="none"/></svg>65</span></div>
</article>
<article class="abs card" style="left:305px">
  <div class="img" role="img" aria-label="Ruins of a columned Greek temple under a cloudy sky" style="background:linear-gradient(180deg,#5e6672,#9aa3ad 45%,#c9bfa8 65%,#7b7a6a)"></div>
  <div class="band">Greece</div>
  <p class="text">Sed ut perspiciatis unde omnis iste natus error sit voluptatem edusa accusant.</p>
  <div class="sep"></div>
  <a class="btn more" href="#" style="text-decoration:none">More</a>
  <div class="stats"><span><svg width="7" height="6" viewBox="0 0 7 6"><path d="M3.5 6 L0.5 3 A1.6 1.6 0 0 1 3.5 1 A1.6 1.6 0 0 1 6.5 3 Z" fill="#8a8a8a"/></svg>457</span><span><svg width="7" height="5" viewBox="0 0 7 5"><rect width="7" height="5" fill="#8a8a8a"/><path d="M0 0 L3.5 3 L7 0" stroke="#232323" stroke-width=".8" fill="none"/></svg>65</span></div>
</article>
<article class="abs card" style="left:514px">
  <div class="img" role="img" aria-label="Carved stone temple pillars in India" style="background:linear-gradient(90deg,#6a4530,#a8725a 40%,#7e5038 70%,#b3876a)"></div>
  <div class="band">India</div>
  <p class="text">Sed ut perspiciatis unde omnis iste natus error sit voluptatem edusa accusant.</p>
  <div class="sep"></div>
  <a class="btn more" href="#" style="text-decoration:none">More</a>
  <div class="stats"><span><svg width="7" height="6" viewBox="0 0 7 6"><path d="M3.5 6 L0.5 3 A1.6 1.6 0 0 1 3.5 1 A1.6 1.6 0 0 1 6.5 3 Z" fill="#8a8a8a"/></svg>457</span><span><svg width="7" height="5" viewBox="0 0 7 5"><rect width="7" height="5" fill="#8a8a8a"/><path d="M0 0 L3.5 3 L7 0" stroke="#232323" stroke-width=".8" fill="none"/></svg>65</span></div>
</article>

<footer class="abs footer"></footer>
<div class="abs foot-plate"><span class="brand-name">Brisk<br>Loom</span></div>
<nav class="abs foot-links">
  <a href="#">Home</a><a href="#">Ancient Arts</a><a href="#">History</a><a href="#">News</a><a href="#">Gallery</a><a href="#">Articles</a><a href="#">Contact</a>
</nav>
<p class="abs copyright">© 2017 BRISK LOOM. ALL RIGHTS RESERVED.</p>
<span class="abs social" style="left:653px" aria-label="Share link"></span>
<span class="abs social" style="left:672px" aria-label="Share link"></span>
<span class="abs social" style="left:691px" aria-label="Share link"></span>

</body>
</html>
```